Redesign one screen in a mobile app

I have an app called Toasts and Tallies (available on iOS and Android). This app allows wedding guests to bet on things that happen during a wedding they are attending (think: will the groom cry when the bride walks down the aisle...). The event is set up by someone called the "event leader", typically this is the bride or the groom.

Once event details, bets, and $ values of the bets are entered, the event leader publishes the event and gets to the event detail homescreen, where they can manage their event. The three main things they can do are:

1.) Share the event with other guests to join in the betting.
2.) Edit the event -- add, change, or delete bets.
3.) Add a co-organizer. If you are the bride or the groom, you want someone else managing the event on your wedding day.

I'd like to redesign this page, make it simpler, and *focus attention on sharing the event.* The biggest goal of this page is getting event leaders to share the event. We want them to invite as many wedding guests as possible.

To that end, I would like to also introducing "sharing tiers" to entice more sharing and I'd like this to be something event leaders can easily see once they hit the event homescreen. Tiers are as follows:
Share with 1 guest, unlock co-organizer feature.
Share with 5 guests, unlock physical placard with custom QR code.
Share with 10 guests, we split our proceeds with the bride and groom.
Share with 20 guests, you are entered into $250 monthly raffle.

Some additional requests:
+ Please do not use current fonts. We want new fonts that are cleaner.
+ Share options should stay the same (copy, share, QR code)
+ Need to keep "help" question mark on page as well.
+ Maintain colors generally. Red button color must be kept as is because it's used throughout app. Slight variations to other colors OK.
+ Navigation at bottom must remain.
+ Feel free to add moving elements as well, like gifs.
+ Final design delivered in Figma.
Updates

Submissions need to be app designs. Not webpages.

The current actions shown on the page need to remain - share event, edit event, add a Co-Organizer. But the goal of the design is to make the page simpler, not more complicated.

Sharing tiers can be a separate screen, linked from the event home screen. This information does not need to live on the same page!

Target Market(s)

25-40 year olds

Industry/Entity Type

Mobile Apps - Betting

Font styles to use
Sans Serif
Other font styles liked:
• I like poppins, but open to other options.

Requirements
Must have
• Fun design that focuses on sharing an event. Design delievered in Figma.

```html
<!DOCTYPE html>
<html lang="en">
<head>
<meta charset="utf-8">
<title>Toasts and Tallies – Event Details</title>
<link href="https://fonts.googleapis.com/css2?family=Poppins:wght@400;500;600;700&display=swap" rel="stylesheet">
<style>
:root{
  --bg:#f2f3f8;
  --card:#ffffff;
  --ink:#111318;
  --ink-soft:#3c4150;
  --muted:#5a5f6b;
  --red:#e05d52;
  --tier:#f4f4f7;
  --check-off:#d6d7db;
  --check-on:#3cb35a;
  --chip:#f1f1f4;
}
*{box-sizing:border-box;margin:0;padding:0}
html,body{width:1200px;height:4277px;overflow:hidden}
body{background:var(--bg);font-family:'Poppins',sans-serif;color:var(--ink);position:relative}
.abs{position:absolute}
.status-time{left:74px;top:14px;font-size:38px;font-weight:500}
.status-icons{right:70px;top:20px}
.round-btn{width:154px;height:154px;border-radius:50%;background:var(--card);display:flex;align-items:center;justify-content:center}
.section-title{left:65px;font-size:54px;font-weight:600;letter-spacing:-.5px}
.card{left:65px;width:1068px;background:var(--card);border-radius:80px}
.event-photo{left:138px;top:551px;width:335px;height:341px;background:linear-gradient(135deg,#dfe3ea 0%,#c9a85c 45%,#8a6a2c 60%,#e8ebf0 100%)}
.event-name{left:523px;top:596px;font-size:62px;font-weight:600;line-height:80px;color:var(--ink-soft)}
.meta{font-size:29px;font-weight:600;color:var(--ink-soft);display:flex;align-items:center;gap:14px}
.location{left:222px;top:955px;font-size:44px;font-weight:600;color:var(--ink-soft)}
.about-title{left:222px;top:1068px;font-size:44px;font-weight:600;color:var(--ink-soft)}
.body-text{font-size:37px;line-height:56px;color:var(--muted)}
.red-btn{background:var(--red);color:#fff;border-radius:22px;height:128px;display:flex;align-items:center}
.joined{left:141px;top:1905px;font-size:37px;color:var(--red);display:flex;align-items:center;gap:18px}
.share-with{left:141px;top:2278px;font-size:36px;font-weight:700}
.tier{left:138px;width:920px;height:97px;background:var(--tier);border-radius:12px;display:flex;align-items:center;justify-content:space-between;padding:0 30px 0 37px;font-size:24px;color:var(--ink)}
.org-label{left:138px;top:3585px;font-size:36px;font-weight:700;color:var(--red)}
.avatar{left:166px;top:3694px;width:172px;height:172px;border-radius:50%;background:linear-gradient(160deg,#6fb0d8,#3b7fa8)}
.add-org{left:446px;top:3694px;width:172px;height:172px;border-radius:50%;background:var(--chip);display:flex;align-items:center;justify-content:center}
.org-name{left:140px;top:3887px;width:224px;text-align:center;font-size:36px;font-weight:600;color:var(--ink-soft)}
.nav{left:0;top:4052px;width:1200px;height:260px;background:var(--card);border-radius:80px 80px 0 0}
.nav-home{left:190px;top:4088px;width:154px;height:154px;border-radius:50%;background:var(--red);display:flex;align-items:center;justify-content:center}
.nav-item{width:200px;text-align:center;font-size:23px;font-weight:600;display:flex;flex-direction:column;align-items:center;gap:8px}
</style>
</head>
<body>

<div class="abs status-time">9:30</div>
<svg class="abs status-icons" width="130" height="44" viewBox="0 0 130 44">
  <path d="M0 8 Q25 -6 50 8 L25 40 Z" fill="#6b6e76"/>
  <path d="M98 4 V40 H60 Z" fill="#222"/>
  <rect x="108" y="6" width="20" height="36" rx="3" fill="#222"/>
</svg>

<div class="abs round-btn" style="left:63px;top:120px">
  <svg width="60" height="60" viewBox="0 0 24 24" fill="none" stroke="#111" stroke-width="2.2" stroke-linecap="round" stroke-linejoin="round"><path d="M20 12H4M10 5l-7 7 7 7"/></svg>
</div>
<div class="abs round-btn" style="left:978px;top:120px">
  <svg width="70" height="70" viewBox="0 0 24 24" fill="none" stroke="#111" stroke-width="2" stroke-linecap="round"><circle cx="12" cy="12" r="10"/><path d="M9.3 9.3a2.8 2.8 0 1 1 3.7 2.6c-.7.3-1 .9-1 1.6v.6"/><circle cx="12" cy="17.3" r=".6" fill="#111"/></svg>
</div>

<h1 class="abs section-title" style="top:335px">Event Details</h1>

<section class="abs card" style="top:477px;height:1110px"></section>
<div class="abs event-photo" role="img" aria-label="Photo of two gold wedding rings"></div>
<h2 class="abs event-name">Arjun &amp; Leela<br>Wedding Day</h2>
<div class="abs meta" style="left:523px;top:803px">
  <svg width="42" height="42" viewBox="0 0 24 24" fill="none" stroke="#3c4150" stroke-width="1.8"><rect x="3" y="5" width="18" height="16" rx="2"/><path d="M3 10h18M8 3v4M16 3v4"/></svg>Feb 21
</div>
<div class="abs meta" style="left:735px;top:803px">
  <svg width="42" height="42" viewBox="0 0 24 24" fill="none" stroke="#3c4150" stroke-width="1.8"><circle cx="12" cy="12" r="9"/><path d="M12 7v5l3 2"/></svg>08:00 PM
</div>
<svg class="abs" style="left:140px;top:962px" width="44" height="46" viewBox="0 0 24 24" fill="none" stroke="#3c4150" stroke-width="1.8"><path d="M12 22s7-6.5 7-12a7 7 0 0 0-14 0c0 5.5 7 12 7 12z"/><circle cx="12" cy="10" r="2.5"/></svg>
<div class="abs location">Jaipur</div>
<svg class="abs" style="left:140px;top:1068px" width="44" height="44" viewBox="0 0 24 24" fill="none" stroke="#3c4150" stroke-width="1.8"><rect x="4" y="3" width="16" height="18" rx="3"/><path d="M8.5 8a3.5 3.5 0 0 0 7 0"/></svg>
<div class="abs about-title">About the Event</div>
<p class="abs body-text" style="left:222px;top:1142px;width:840px">Lorem ipsum dolor sit amet, consectetur adipiscing elit, sed do eiusmod tempor incididunt ut labore et dolore magna aliqua.</p>
<div class="abs red-btn" style="left:141px;top:1384px;width:918px;padding:0 67px 0 45px;justify-content:space-between">
  <span style="display:flex;align-items:center;gap:22px;font-size:35px">
    <svg width="46" height="48" viewBox="0 0 24 24" fill="none" stroke="#fff" stroke-opacity=".75" stroke-width="1.6"><rect x="3" y="3" width="11" height="15" rx="1.5"/><rect x="9" y="6" width="11" height="15" rx="1.5"/></svg>5 Bets</span>
  <span style="font-size:35px;font-weight:600">Edit your Event</span>
</div>

<h2 class="abs section-title" style="top:1665px">Share your Event</h2>
<section class="abs card" style="top:1806px;height:1269px"></section>
<div class="abs joined">
  <svg width="52" height="44" viewBox="0 0 26 22" fill="none" stroke="#e05d52" stroke-width="1.6" stroke-linecap="round"><circle cx="10" cy="7" r="4"/><path d="M2 20c0-4 3.5-6.5 8-6.5s8 2.5 8 6.5M17 3.2a4 4 0 0 1 0 7.6M20 13.8c2.4.8 4 2.8 4 6.2"/></svg>3 People Joined
</div>
<p class="abs body-text" style="left:141px;top:2010px;width:900px">Invite guests to join by sharing the event below. Each guest pays $2.99 to join, and if 10+ guests join in the fun, we share the proceeds with the bride and groom!</p>
<div class="abs share-with">Share with</div>

<div class="abs tier" style="top:2369px"><span>1 guest, Become an organiser</span>
  <svg width="38" height="38" viewBox="0 0 24 24"><circle cx="12" cy="12" r="12" fill="var(--check-on)"/><path d="M7 12.5l3.3 3.3L17 9" fill="none" stroke="#fff" stroke-width="2.4" stroke-linecap="round"/></svg></div>
<div class="abs tier" style="top:2480px"><span>5 guests, unlock physical placard with custom QR code.</span>
  <svg width="38" height="38" viewBox="0 0 24 24"><circle cx="12" cy="12" r="12" fill="var(--check-off)"/><path d="M7 12.5l3.3 3.3L17 9" fill="none" stroke="#fff" stroke-width="2.4" stroke-linecap="round"/></svg></div>
<div class="abs tier" style="top:2591px"><span>10 guests, we split our proceeds with the bride and groom.</span>
  <svg width="38" height="38" viewBox="0 0 24 24"><circle cx="12" cy="12" r="12" fill="var(--check-off)"/><path d="M7 12.5l3.3 3.3L17 9" fill="none" stroke="#fff" stroke-width="2.4" stroke-linecap="round"/></svg></div>
<div class="abs tier" style="top:2702px"><span>20 guests, you are entered into $250 monthly raffle.</span>
  <svg width="38" height="38" viewBox="0 0 24 24"><circle cx="12" cy="12" r="12" fill="var(--check-off)"/><path d="M7 12.5l3.3 3.3L17 9" fill="none" stroke="#fff" stroke-width="2.4" stroke-linecap="round"/></svg></div>

<div class="abs red-btn" style="left:138px;top:2852px;width:917px;justify-content:center;font-size:35px;font-weight:600">Share</div>

<h2 class="abs section-title" style="top:3153px">Assign a Co-Organiser</h2>
<section class="abs card" style="top:3296px;height:704px"></section>
<p class="abs body-text" style="left:138px;top:3357px;width:920px">Lorem ipsum dolor sit amet, consectetur adipiscing elit, sed do eiusmod tempor incididunt ut labore et dolore magna aliqua.</p>
<div class="abs org-label">Event Organizers</div>
<div class="abs avatar" role="img" aria-label="Profile photo of organiser Tom Reyes"></div>
<div class="abs org-name">Tom Reyes</div>
<div class="abs add-org">
  <svg width="56" height="56" viewBox="0 0 24 24" stroke="#e05d52" stroke-width="2" stroke-linecap="round"><path d="M12 4v16M4 12h16"/></svg>
</div>

<nav class="abs nav"></nav>
<div class="abs nav-home">
  <svg width="66" height="66" viewBox="0 0 24 24" fill="none" stroke="#fff" stroke-opacity=".85" stroke-width="1.4" stroke-linejoin="round"><path d="M4 10l8-6 8 6v9a2 2 0 0 1-2 2H6a2 2 0 0 1-2-2z"/><path d="M10 17h4" stroke-linecap="round"/></svg>
</div>
<div class="abs nav-item" style="left:493px;top:4104px">
  <svg width="64" height="70" viewBox="0 0 24 26" fill="none" stroke="#111" stroke-width="1.4"><rect x="3" y="2" width="11" height="16" rx="1.5"/><rect x="9" y="6" width="11" height="17" rx="1.5" fill="#fff"/></svg>My Bets
</div>
<div class="abs nav-item" style="left:792px;top:4104px">
  <svg width="66" height="70" viewBox="0 0 24 26" fill="none" stroke="#111" stroke-width="1.3" stroke-linejoin="round"><path d="M12 2l1.3 2.6 2.8.4-2 2 .5 2.8L12 8.5 9.4 9.8l.5-2.8-2-2 2.8-.4z"/><rect x="9" y="12" width="6" height="12"/><rect x="3" y="16" width="6" height="8"/><rect x="15" y="18" width="6" height="6"/></svg>My Bets
</div>

</body>
</html>
```